Social house sales

An app that allows someone to search for houses for sale in a certain city or post code...then returns the results and allows the user to like or comment on each property for sale, and @mention others who are users.
UPDATE:
May i know whats your apps name?and please attach the logo.
also - No logo yet! But the name is ''Pelko''
can i get more specific how many pages you want? - Five pages of the mocked up is fine
can you provide the wireframe? - I haven''t done any wire frames, looking for inspiration! Registration/opening splash page, search page, results page, comment/liking, @mentioning someone - those could be five views
and are this app have profile page? No
login with qm or brindlo or vaultspan? QM
which OS i should design it? (IOS,Android) iOS
House buyers, renters
House

```html
<!DOCTYPE html>
<html lang="en">
<head>
<meta charset="utf-8">
<title>Pelko – Search</title>
<link rel="stylesheet" href="https://fonts.googleapis.com/css2?family=Roboto:wght@400;500&display=swap">
<style>
  :root {
    --purple: #846cbf;
    --purple-deep: #4b2f8c;
    --ink: #141414;
    --muted: #7a7a7a;
    --chevron: #b9b9b9;
    --rule: #dedede;
    --band: #f3f3f4;
    --white: #ffffff;
    --statusbar: #000000;
    --icon: #555555;
  }
  * { box-sizing: border-box; margin: 0; padding: 0; }
  html, body { width: 683px; height: 1200px; overflow: hidden; }
  body {
    font-family: "Roboto", Arial, sans-serif;
    background: var(--band);
    color: var(--ink);
    display: flex;
    flex-direction: column;
  }
  .status-bar {
    height: 50px; background: var(--statusbar); color: var(--white);
    display: flex; align-items: center; justify-content: space-between;
    padding: 0 14px; font-weight: 500; font-size: 24px; position: relative;
  }
  .status-bar .carrier { display: flex; align-items: center; gap: 6px; }
  .status-bar .time { position: absolute; left: 50%; transform: translateX(-50%); }
  .status-bar .indicators { display: flex; align-items: center; gap: 10px; }
  .app-header {
    height: 96px; background: var(--purple); color: var(--white);
    display: flex; align-items: center; justify-content: center; position: relative;
    font-size: 31px;
  }
  .app-header .back { position: absolute; left: 34px; top: 50%; transform: translateY(-50%); }
  .search-field {
    height: 91px; background: var(--white); display: flex; align-items: center;
    padding-left: 32px; gap: 24px; font-size: 29px; color: var(--muted);
    border-bottom: 1px solid var(--rule);
  }
  .section-label {
    height: 84px; display: flex; align-items: flex-end; padding: 0 0 20px 35px;
    font-size: 27px; color: #555; letter-spacing: 0.5px;
    border-bottom: 1px solid var(--rule);
  }
  .filter-list { list-style: none; background: var(--white); }
  .filter-row {
    height: 90px; display: flex; align-items: center; justify-content: space-between;
    padding: 0 30px 0 35px; border-bottom: 1px solid var(--rule); font-size: 32px;
  }
  .filter-row .value { display: flex; align-items: center; gap: 22px; color: var(--muted); }
  .action-area { height: 143px; display: flex; align-items: center; justify-content: center; border-bottom: 1px solid var(--rule); }
  .search-button {
    width: 605px; height: 94px; background: var(--purple); color: var(--white);
    border: none; border-bottom: 4px solid var(--purple-deep); border-radius: 3px;
    font-family: inherit; font-size: 33px; letter-spacing: 0.5px; margin-top: -20px;
  }
  .tab-bar {
    flex: 1; background: #f7f7f8; display: flex; align-items: center; justify-content: space-around;
    padding: 0 20px;
  }
</style>
</head>
<body>
  <div class="status-bar">
    <div class="carrier">
      <svg width="42" height="18" viewBox="0 0 42 18" fill="#fff">
        <rect x="0" y="12" width="5" height="6"/><rect x="8" y="9" width="5" height="9"/>
        <rect x="16" y="6" width="5" height="12"/><rect x="24" y="3" width="5" height="15"/>
        <rect x="32" y="0" width="5" height="18"/>
      </svg>
      <span>KG</span>
    </div>
    <div class="time">1:57 PM</div>
    <div class="indicators">
      <svg width="22" height="22" viewBox="0 0 22 22"><circle cx="11" cy="11" r="10" fill="#fff"/><path d="M11 5v6h4" stroke="#000" stroke-width="2.4" fill="none"/></svg>
      <svg width="22" height="22" viewBox="0 0 22 22"><path d="M21 1 1 10l9 2 2 9z" fill="#fff"/></svg>
      <svg width="26" height="26" viewBox="0 0 26 26" fill="none" stroke="#fff" stroke-width="2.4"><path d="M22 13a9 9 0 1 1-4-7.5"/><path d="M18 2v4h-4"/><rect x="9" y="12" width="8" height="7" fill="#fff" stroke="none"/><path d="M10.5 12v-2a2.5 2.5 0 0 1 5 0v2"/></svg>
      <svg width="44" height="20" viewBox="0 0 44 20"><rect x="1" y="1" width="38" height="18" rx="2" fill="none" stroke="#fff" stroke-width="2"/><rect x="4" y="4" width="32" height="12" fill="#fff"/><rect x="40" y="6" width="3" height="8" fill="#fff"/></svg>
    </div>
  </div>

  <header class="app-header">
    <svg class="back" width="44" height="44" viewBox="0 0 44 44" fill="none" stroke="#fff" stroke-width="2.4">
      <circle cx="22" cy="22" r="20"/><path d="M31 22H13M20 15l-7 7 7 7"/>
    </svg>
    <h1 style="font-weight:400;font-size:31px;">Search</h1>
  </header>

  <div class="search-field">
    <svg width="34" height="34" viewBox="0 0 34 34" fill="none" stroke="#9a9a9a" stroke-width="2.6"><circle cx="14" cy="14" r="11"/><path d="M22 22l10 10"/></svg>
    <span>City, Address or Postal Code</span>
  </div>

  <div class="section-label">CATEGORY</div>

  <ul class="filter-list">
    <li class="filter-row"><span>Property Type</span><span class="value">Freehold<svg width="14" height="22" viewBox="0 0 14 22" fill="none" stroke="var(--chevron)" stroke-width="3"><path d="M2 2l9 9-9 9"/></svg></span></li>
    <li class="filter-row"><span>Listing Type</span><span class="value">Sale<svg width="14" height="22" viewBox="0 0 14 22" fill="none" stroke="var(--chevron)" stroke-width="3"><path d="M2 2l9 9-9 9"/></svg></span></li>
    <li class="filter-row"><span>Price</span><span class="value">Any<svg width="14" height="22" viewBox="0 0 14 22" fill="none" stroke="var(--chevron)" stroke-width="3"><path d="M2 2l9 9-9 9"/></svg></span></li>
    <li class="filter-row"><span>Bedrooms</span><span class="value">Any<svg width="14" height="22" viewBox="0 0 14 22" fill="none" stroke="var(--chevron)" stroke-width="3"><path d="M2 2l9 9-9 9"/></svg></span></li>
    <li class="filter-row"><span>Bathrooms</span><span class="value">Any<svg width="14" height="22" viewBox="0 0 14 22" fill="none" stroke="var(--chevron)" stroke-width="3"><path d="M2 2l9 9-9 9"/></svg></span></li>
    <li class="filter-row"><span>Days On Market</span><span class="value">Any<svg width="14" height="22" viewBox="0 0 14 22" fill="none" stroke="var(--chevron)" stroke-width="3"><path d="M2 2l9 9-9 9"/></svg></span></li>
    <li class="filter-row"><span>Features</span><span class="value">Any<svg width="14" height="22" viewBox="0 0 14 22" fill="none" stroke="var(--chevron)" stroke-width="3"><path d="M2 2l9 9-9 9"/></svg></span></li>
  </ul>

  <div class="action-area">
    <button class="search-button">SEARCH PROPERTIES</button>
  </div>

  <nav class="tab-bar">
    <svg width="56" height="56" viewBox="0 0 56 56" fill="none" stroke="var(--purple)" stroke-width="3"><circle cx="22" cy="22" r="17"/><path d="M34 34l18 18"/></svg>
    <svg width="52" height="52" viewBox="0 0 52 52" fill="none" stroke="var(--icon)" stroke-width="2.2"><circle cx="26" cy="26" r="23"/><path d="M20 20a6 6 0 1 1 8 5.7c-1.5.6-2 1.6-2 3.3v2"/><circle cx="26" cy="37" r="1.5" fill="var(--icon)"/></svg>
    <svg width="56" height="50" viewBox="0 0 56 50" fill="none" stroke="var(--icon)" stroke-width="2.2"><path d="M28 46 6 24A12 12 0 0 1 28 9a12 12 0 0 1 22 15z"/></svg>
    <svg width="54" height="50" viewBox="0 0 54 50" fill="none" stroke="var(--icon)" stroke-width="2.2"><path d="M38 30v16H3V16h10"/><path d="M12 34c2-12 12-18 26-18V8l13 12-13 12v-8c-11 0-19 3-26 10z"/></svg>
    <svg width="54" height="48" viewBox="0 0 54 48" fill="none" stroke="var(--icon)" stroke-width="2.2"><path d="M27 4C14 4 3 12 3 22c0 6 4 11 10 14l-3 9 11-7c2 .4 4 .6 6 .6 13 0 24-8 24-16.6S40 4 27 4z"/></svg>
  </nav>
</body>
</html>
```